drafting business needs a 2 sided rack card design. Size specificaton

Document Trim Size:
Full Bleed Size (starting document size)
3.86" x 8.39"
When trimmed the Rack cards are 3.74" x 8.27".
300 DPI

I need my logo, product info, and 2 pictures included

This is product information that i need:

- Floor Plans measured to KEDV & TRUZ standards
- Stunning HD Photography
- Vistaloom - your space delivered in perfect 3D
- E &O insured
- Our products delivered next by before 10:00 AM

It also has to my my special offer: Save 50% off Vistaloom, Floor Plans, and Photography

My contact info is
www.tidewellplans-demo.com
dorian@tidewellplans-demo.com
555-014-2286

Hey designers, the common element I see in most of the designs that I actually don't like is the use of orange and blue. I think there was some miscommunication. Please Don't use these colors. It really makes the designs Look cheap. I want a clean, high end look.

realtors

Real Estate

Serif

• At least 2 photos and my logo included. it must include all my wording with discount in bold, but classy.
• I want clean classy design. My logo is and 2 photos should be in design. I design should match my logo colors, I think. I have tons of other photos if you think these arent very useful
• Also I have attached a logo from vistaloom. Please include this, but smaller than the Tidewell Plans. The Vistaloom is just equiptment that I use
• This is a discount promotion, but I dont want it to look cheap whatsoever

```html
<!DOCTYPE html>
<html lang="en">
<head>
<meta charset="utf-8">
<title>Tidewell Plans Rack Card</title>
<link rel="stylesheet" href="https://fonts.googleapis.com/css2?family=Rokkitt:wght@400;500;700&family=Montserrat:wght@500;600&display=swap">
<style>
  :root {
    --stage: #2b2b2b;
    --paper: #ffffff;
    --slate: #34414a;
    --slate-soft: #56646d;
    --gold: #b8975a;
    --sand: #dccab0;
    --ink: #222222;
    --body: #333333;
    --on-dark: #ffffff;
    --serif: "Rokkitt", Georgia, serif;
    --sans: "Montserrat", Arial, sans-serif;
  }
  * { box-sizing: border-box; margin: 0; padding: 0; }
  html, body { width: 1200px; height: 1200px; overflow: hidden; background: var(--stage); }
  .stage { position: relative; width: 1200px; height: 1200px; }
  .card {
    position: absolute; top: 130px; width: 443px; height: 962px;
    background: linear-gradient(180deg, #f4f5f6 0%, #ffffff 55%, #f7f7f7 100%);
    overflow: hidden;
  }
  .card--front { left: 101px; }
  .card--back { left: 630px; }
  .card svg.shapes { position: absolute; inset: 0; }

  .brand { position: absolute; left: 200px; top: 14px; width: 230px; text-align: center; }
  .brand__mark { width: 66px; height: 66px; border-radius: 50%; background: var(--gold); margin: 0 auto 4px; }
  .brand__name { font-family: var(--serif); font-weight: 400; font-size: 30px; color: var(--slate); white-space: nowrap; }

  .offer {
    position: absolute; left: 31px; top: 638px; width: 372px; height: 164px;
    background: var(--gold); border-radius: 28px;
    box-shadow: 0 14px 16px -10px rgba(0,0,0,.25);
  }
  .offer::before {
    content: ""; position: absolute; inset: 9px;
    border: 2px dashed var(--ink); border-radius: 22px;
  }
  .offer__save { position: absolute; left: 28px; top: 24px; font-family: var(--serif); font-size: 56px; line-height: 1; color: var(--on-dark); }
  .offer__pct { position: absolute; left: 22px; top: 78px; font-family: var(--serif); font-weight: 700; font-size: 70px; line-height: 1; color: var(--ink); }
  .offer__off {
    position: absolute; left: 190px; top: 28px; width: 35px; height: 106px;
    background: var(--ink); color: var(--on-dark); font-family: var(--serif); font-size: 30px;
    line-height: 34px; text-align: center; padding-top: 3px;
  }
  .offer__list { position: absolute; left: 236px; top: 32px; list-style: none; font-family: var(--serif); font-weight: 500; font-size: 18px; color: var(--ink); }
  .offer__list li { height: 37px; }
  .offer__list li::before { content: "•"; color: var(--on-dark); margin-right: 6px; }

  .contact { position: absolute; right: 20px; top: 858px; text-align: right; }
  .contact__title { font-family: var(--serif); font-weight: 500; font-size: 17px; color: var(--gold); margin-bottom: 6px; margin-right: 22px; }
  .contact__line { display: flex; justify-content: flex-end; align-items: center; gap: 5px; font-family: var(--sans); font-weight: 600; font-size: 11px; color: var(--on-dark); height: 21px; white-space: nowrap; }
  .contact__icon { width: 17px; height: 17px; flex: none; }

  .services-tab {
    position: absolute; left: 0; top: 576px; width: 162px; height: 30px;
    background: var(--gold); border-radius: 0 15px 15px 0;
    font-family: var(--serif); font-weight: 500; font-size: 16px; color: var(--on-dark);
    padding-left: 28px; line-height: 31px;
  }
  .services { position: absolute; left: 33px; top: 624px; list-style: none; font-family: var(--serif); font-size: 16px; color: var(--body); }
  .services li { height: 36px; display: flex; align-items: center; }
  .services li::before { content: ""; width: 7px; height: 7px; border-radius: 50%; background: var(--gold); margin-right: 10px; flex: none; }
</style>
</head>
<body>
<main class="stage">

  <section class="card card--front">
    <svg class="shapes" width="443" height="962" viewBox="0 0 443 962">
      <defs>
        <linearGradient id="livingRoom" x1="0" y1="0" x2="1" y2="1">
          <stop offset="0" stop-color="#dde4e8"/>
          <stop offset=".5" stop-color="#e8e3da"/>
          <stop offset="1" stop-color="#6f5a48"/>
        </linearGradient>
        <linearGradient id="bedroom" x1="0" y1="0" x2="0" y2="1">
          <stop offset="0" stop-color="#e9e1d9"/>
          <stop offset=".55" stop-color="#c9b4ad"/>
          <stop offset="1" stop-color="#b39a97"/>
        </linearGradient>
      </defs>
      <circle cx="213" cy="342" r="222" fill="none" stroke="#b8975a" stroke-width="5"/>
      <circle cx="213" cy="342" r="214" fill="url(#livingRoom)" role="img" aria-label="Photo of a bright living room with sofa and tall windows"/>
      <circle cx="-8" cy="96" r="192" fill="#34414a" opacity=".85"/>
      <circle cx="342" cy="503" r="108" fill="#34414a"/>
      <circle cx="342" cy="503" r="101" fill="#fff"/>
      <circle cx="342" cy="503" r="96" fill="url(#bedroom)" role="img" aria-label="Photo of a bedroom with made bed and round mirror"/>
      <circle cx="350" cy="1060" r="240" fill="#34414a"/>
      <circle cx="80" cy="968" r="92" fill="#dccab0" opacity=".85"/>
    </svg>

    <div class="brand">
      <div class="brand__mark"></div>
      <div class="brand__name">Tidewell Plans</div>
    </div>

    <div class="offer">
      <div class="offer__save">SAVE</div>
      <div class="offer__pct">50%</div>
      <div class="offer__off">O<br>F<br>F</div>
      <ul class="offer__list">
        <li>Vistaloom</li>
        <li>Floor Plans</li>
        <li>Photography</li>
      </ul>
    </div>

    <div class="contact">
      <div class="contact__title">CONTACT US</div>
      <div class="contact__line">555-014-2286
        <svg class="contact__icon" viewBox="0 0 18 18"><circle cx="9" cy="9" r="8" fill="none" stroke="#b8975a" stroke-width="1.4"/><rect x="6" y="4" width="6" height="10" rx="1.2" fill="none" stroke="#b8975a" stroke-width="1.3"/></svg></div>
      <div class="contact__line">dorian@tidewellplans-demo.com
        <svg class="contact__icon" viewBox="0 0 18 18"><circle cx="9" cy="9" r="8" fill="none" stroke="#b8975a" stroke-width="1.4"/><rect x="4.5" y="6" width="9" height="6.5" fill="none" stroke="#b8975a" stroke-width="1.3"/><path d="M4.5 6 9 10l4.5-4" fill="none" stroke="#b8975a" stroke-width="1.3"/></svg></div>
      <div class="contact__line">www.tidewellplans-demo.com
        <svg class="contact__icon" viewBox="0 0 18 18"><circle cx="9" cy="9" r="8" fill="none" stroke="#b8975a" stroke-width="1.4"/><circle cx="9" cy="9" r="4.5" fill="none" stroke="#b8975a" stroke-width="1.2"/><path d="M4.5 9h9M9 4.5v9" stroke="#b8975a" stroke-width="1"/></svg></div>
    </div>
  </section>

  <section class="card card--back">
    <svg class="shapes" width="443" height="962" viewBox="0 0 443 962">
      <defs>
        <linearGradient id="entryHall" x1="0" y1="0" x2="1" y2="1">
          <stop offset="0" stop-color="#8a5a3a"/>
          <stop offset=".35" stop-color="#efe9df"/>
          <stop offset=".7" stop-color="#e3dbcf"/>
          <stop offset="1" stop-color="#7a4a28"/>
        </linearGradient>
      </defs>
      <rect x="0" y="0" width="443" height="232" fill="#34414a" opacity=".85"/>
      <circle cx="62" cy="422" r="108" fill="#56646d" opacity=".8"/>
      <rect x="0" y="232" width="62" height="190" fill="#56646d" opacity=".8"/>
      <circle cx="227" cy="283" r="240" fill="#fff"/>
      <circle cx="227" cy="283" r="240" fill="none" stroke="#b8975a" stroke-width="6"/>
      <circle cx="227" cy="283" r="229" fill="url(#entryHall)" role="img" aria-label="Photo looking down into an entry hall with staircase, bench and painting"/>
      <circle cx="350" cy="1060" r="240" fill="#34414a"/>
      <circle cx="80" cy="966" r="92" fill="#dccab0" opacity=".85"/>
    </svg>

    <div class="services-tab">OUR SERVICES</div>
    <ul class="services">
      <li>Floor Plans measured to KEDV &amp; TRUZ standards</li>
      <li>Stunning HD Photography</li>
      <li>Vistaloom - your space delivered in perfect 3D</li>
      <li>E &amp;O insured</li>
      <li>Our products delivered next by before 10:00 AM</li>
    </ul>

    <div class="contact">
      <div class="contact__title">CONTACT US</div>
      <div class="contact__line">555-014-2286
        <svg class="contact__icon" viewBox="0 0 18 18"><circle cx="9" cy="9" r="8" fill="none" stroke="#b8975a" stroke-width="1.4"/><rect x="6" y="4" width="6" height="10" rx="1.2" fill="none" stroke="#b8975a" stroke-width="1.3"/></svg></div>
      <div class="contact__line">dorian@tidewellplans-demo.com
        <svg class="contact__icon" viewBox="0 0 18 18"><circle cx="9" cy="9" r="8" fill="none" stroke="#b8975a" stroke-width="1.4"/><rect x="4.5" y="6" width="9" height="6.5" fill="none" stroke="#b8975a" stroke-width="1.3"/><path d="M4.5 6 9 10l4.5-4" fill="none" stroke="#b8975a" stroke-width="1.3"/></svg></div>
      <div class="contact__line">www.tidewellplans-demo.com
        <svg class="contact__icon" viewBox="0 0 18 18"><circle cx="9" cy="9" r="8" fill="none" stroke="#b8975a" stroke-width="1.4"/><circle cx="9" cy="9" r="4.5" fill="none" stroke="#b8975a" stroke-width="1.2"/><path d="M4.5 9h9M9 4.5v9" stroke="#b8975a" stroke-width="1"/></svg></div>
    </div>
  </section>

</main>
</body>
</html>
```